Bright Meadow Care Partners, LLC

We are private duty home care agency. We provide in-home care for people of all ages. Our kind natured and patient caregivers provide assistance to those who have difficulty with caring for themselves. We already have a logo designed by ArtNestly

```html
<!DOCTYPE html>
<html lang="en">
<head>
<meta charset="utf-8">
<title>Bright Meadow Care Partners</title>
<link href="https://fonts.googleapis.com/css2?family=Montserrat:wght@300;400;500;600;700&display=swap" rel="stylesheet">
<style>
:root{
  --green:#3d9b1c;
  --orange:#f47a1f;
  --ink:#3b3b3b;
  --muted:#555;
  --light:#f5f5f5;
  --line:#dcdcdc;
  --hero:#e7ebee;
  --black:#050505;
}
*{margin:0;padding:0;box-sizing:border-box}
html,body{width:1200px;height:2952px;overflow:hidden;background:#fff}
body{font-family:'Montserrat',sans-serif;color:var(--ink);position:relative}
.abs{position:absolute}

/* header */
.site-header{position:absolute;left:0;top:0;width:1200px;height:66px;background:#fff;border-bottom:1px solid #eee}
.corner-dots{left:10px;top:10px;display:flex;gap:8px}
.corner-dots i{width:7px;height:7px;display:block}
.brand{left:124px;top:20px;display:flex;align-items:center;gap:8px;font-weight:700;font-size:17px;color:var(--green);letter-spacing:.2px}
.brand .mark{width:14px;height:14px;background:var(--orange)}
.main-nav{left:478px;top:25px;display:flex;gap:20px;font-size:12px;color:var(--orange);letter-spacing:.3px}
.main-nav .sep{color:#333}
.social{left:1020px;top:27px;display:flex;gap:7px}
.social i{width:8px;height:8px;border-radius:50%;background:#333;display:block}

/* hero */
.hero{left:0;top:66px;width:1200px;height:497px;background:linear-gradient(90deg,#b9aea0 0%,#cfc6b8 18%,#dcd8d2 35%,#e4e6e7 46%,var(--hero) 60%)}
.hero h1{left:547px;top:126px;font-size:36px;font-weight:600;line-height:42px;color:#454545;letter-spacing:.3px}
.hero p{left:547px;top:227px;width:500px;font-size:13.5px;line-height:22px;color:#555}
.btn-green{left:547px;top:331px;width:181px;height:36px;background:var(--green);color:#fff;font-size:12.5px;font-weight:600;letter-spacing:1.5px;display:flex;align-items:center;justify-content:center}
.slide-arrow{top:226px}

/* intro */
.intro{left:0;top:632px;width:1200px;text-align:center;font-size:25px;font-weight:300;line-height:30px;color:#444}

/* features */
.feature{top:823px;width:218px}
.feature .photo{width:218px;height:262px}
.feature h3{margin-top:22px;text-align:center;font-size:15.5px;font-weight:500;letter-spacing:1.8px;color:#333}

/* services */
.services{left:0;top:1234px;width:1200px;height:735px;background:var(--light)}
.services h2{position:absolute;left:0;top:40px;width:1200px;text-align:center;font-size:22px;font-weight:600;color:#444}
.card{position:absolute;width:299px;height:274px;background:#fff;border:1px solid var(--line);text-align:center}
.card svg{position:absolute;left:122px;top:26px}
.card h4{position:absolute;left:0;top:96px;width:100%;font-size:13.5px;font-weight:500;color:#333}
.card p{position:absolute;left:24px;top:135px;width:250px;font-size:11.8px;line-height:17.5px;color:#555}
.card .btn{position:absolute;left:86px;top:216px;width:127px;height:31px;background:var(--orange);color:#fff;font-size:12.5px;font-weight:500;letter-spacing:1.5px;display:flex;align-items:center;justify-content:center}

/* blog */
.blog-lead{left:124px;top:2028px;font-size:20.5px;color:#333}
.btn-outline{border:2px solid var(--orange);color:var(--orange);display:flex;align-items:center;justify-content:center;letter-spacing:1.8px;font-weight:500}
.blog-btn{left:776px;top:2016px;width:180px;height:53px;font-size:13.5px}
.post{top:2109px;width:456px;height:255px;color:#fff}
.post .date{position:absolute;left:25px;top:72px;width:50px;height:50px;border:2px solid #fff;text-align:center}
.post .date b{display:block;font-size:22px;line-height:24px;margin-top:5px;font-weight:600}
.post .date span{font-size:11px;line-height:12px;display:block}
.post h5{position:absolute;left:88px;top:72px;width:340px;font-size:20px;line-height:24px;font-weight:600}
.post p{position:absolute;left:23px;top:138px;font-size:14px}
.post .more{position:absolute;left:25px;top:184px;width:127px;height:29px;background:var(--green);font-size:11px;font-weight:700;letter-spacing:1.4px;display:flex;align-items:center;justify-content:center;gap:10px}

/* testimonial */
.quote-mark{left:132px;top:2452px;font-size:56px;font-weight:700;color:#a6cf8f;line-height:56px}
.t-name{left:176px;top:2450px;font-size:25px;font-weight:600;color:#444}
.t-role{left:176px;top:2490px;font-size:10px;color:#444}
.t-text{left:176px;top:2528px;width:850px;font-size:13.5px;line-height:20px;color:#555}
.dots{left:510px;top:2649px;display:flex;gap:5px}
.dots i{width:42px;height:4px;background:#ddd;display:block}
.dots i.on{background:var(--orange)}
.btn-solid{left:393px;top:2697px;width:185px;height:50px;background:var(--orange);color:#fff;font-size:11px;font-weight:600;letter-spacing:1.8px;display:flex;align-items:center;justify-content:center}
.btn-testi{left:594px;top:2697px;width:184px;height:50px;font-size:11px;font-weight:600}

/* footer */
.site-footer{left:0;top:2838px;width:1200px;height:114px;background:var(--black);color:#fff;text-align:center}
.site-footer .co{position:absolute;top:42px;width:100%;font-size:12px;font-weight:600}
.site-footer .addr{position:absolute;top:59px;width:100%;font-size:11.5px}
.site-footer .copy{position:absolute;top:83px;width:100%;font-size:11px;color:#555;letter-spacing:1.2px}
</style>
</head>
<body>

<header class="site-header">
  <div class="abs corner-dots"><i style="background:var(--green)"></i><i style="background:var(--orange)"></i></div>
  <div class="abs brand"><span class="mark"></span>Bright Meadow Care Partners</div>
  <nav class="abs main-nav">
    <span>ABOUT CARING PEOPLE</span><span class="sep">|</span>
    <span>HOME CARE SERVICES</span><span class="sep">|</span>
    <span>CONTACT US</span>
  </nav>
  <div class="abs social"><i></i><i></i><i></i><i></i></div>
</header>

<section class="abs hero">
  <div class="abs" role="img" aria-label="Caregiver helping a smiling elderly woman walk with a walker" style="left:0;top:0;width:540px;height:497px;background:linear-gradient(90deg,rgba(170,150,120,.35),rgba(210,200,185,.25) 70%,rgba(231,235,238,0))"></div>
  <svg class="abs slide-arrow" style="left:105px" width="22" height="40" viewBox="0 0 22 40"><path d="M20 2 L3 20 L20 38" fill="none" stroke="#fff" stroke-width="3"/></svg>
  <svg class="abs slide-arrow" style="left:1072px" width="22" height="40" viewBox="0 0 22 40"><path d="M2 2 L19 20 L2 38" fill="none" stroke="#fff" stroke-width="3"/></svg>
  <h1 class="abs">IN-HOME PRIVATE DUTY<br>CAREGIVERS</h1>
  <p class="abs">At the Bright Meadow Care Partners, LLC we believe that a small group of caring anddedicated people create a dynamic culture that transforms lives.</p>
  <div class="abs btn-green">FREE CONSULTATION</div>
</section>

<p class="abs intro">We provide in-home care for people of all ages. Our kind natured &amp;<br>patientcaregivers provide assistance to those who have<br>difficulty with caringfor themselves.</p>

<div class="abs feature" style="left:124px"><div class="photo" role="img" aria-label="Nurse hugging a smiling senior woman" style="background:linear-gradient(160deg,#d9d4cc,#5ab3d6 60%,#2b5f9e)"></div><h3>CARE PROCESS</h3></div>
<div class="abs feature" style="left:368px"><div class="photo" role="img" aria-label="Smiling care team of doctor and nurses" style="background:linear-gradient(180deg,#f2f2f2,#d8d3cd 55%,#8fb3d6)"></div><h3>CARE TEAM</h3></div>
<div class="abs feature" style="left:612px"><div class="photo" role="img" aria-label="Senior man using a tablet with a doctor" style="background:linear-gradient(160deg,#c9b9a3,#a9a49c 50%,#e6e2dc)"></div><h3>TECHNOLOGY</h3></div>
<div class="abs feature" style="left:856px"><div class="photo" role="img" aria-label="Teacher with happy children at a table" style="background:linear-gradient(160deg,#6ab04c,#e2553a 50%,#d9a27c)"></div><h3>PROGRAMS</h3></div>

<section class="abs services">
  <h2>CARE SERVICES</h2>

  <div class="card" style="left:125px;top:90px">
    <svg width="54" height="54" viewBox="0 0 54 54" fill="none" stroke="var(--orange)" stroke-width="2.2"><circle cx="30" cy="22" r="18"/><path d="M30 31 l-7-7 a4 4 0 0 1 7-5 a4 4 0 0 1 7 5z"/><path d="M4 44 h10 l10 4 h18 l8-8"/><path d="M4 38 h8 v12 h-8z" fill="var(--orange)"/></svg>
    <h4>Personal Hygiene</h4>
    <p>Lorem ipsum, or lipsum as it is sometimes known, is dummy text used in laying out print, graphic or web designs.</p>
    <div class="btn">READ MORE</div>
  </div>
  <div class="card" style="left:452px;top:90px">
    <svg width="54" height="54" viewBox="0 0 54 54" fill="none" stroke="var(--orange)" stroke-width="2.2"><path d="M10 14 h8 v6 l4 6 v20 h-16 v-20 l4-6z"/><circle cx="34" cy="36" r="10"/><path d="M34 26 q2-6 6-7"/></svg>
    <h4>Meals and Nutrition</h4>
    <p>Lorem ipsum, or lipsum as it is sometimes known, is dummy text used in laying out print, graphic or web designs.</p>
    <div class="btn">READ MORE</div>
  </div>
  <div class="card" style="left:777px;top:90px">
    <svg width="54" height="54" viewBox="0 0 54 54" fill="none" stroke="var(--orange)" stroke-width="2.6"><circle cx="34" cy="8" r="4"/><path d="M24 18 l10-4 l2 14 h8 l2 14"/><path d="M20 26 a12 12 0 1 0 16 16"/></svg>
    <h4>Help with Mobility</h4>
    <p>Lorem ipsum, or lipsum as it is sometimes known, is dummy text used in laying out print, graphic or web designs.</p>
    <div class="btn">READ MORE</div>
  </div>

  <div class="card" style="left:125px;top:417px">
    <svg width="54" height="54" viewBox="0 0 54 54" fill="none" stroke="var(--orange)" stroke-width="2.2"><path d="M14 26 L32 8 L50 26"/><path d="M18 22 v16 h28 v-16"/><path d="M4 36 h8 v14 h-8z"/><path d="M12 40 h12 l8 4 h12"/></svg>
    <h4>Home Maintenance</h4>
    <p>Lorem ipsum, or lipsum as it is sometimes known, is dummy text used in laying out print, graphic or web designs.</p>
    <div class="btn">READ MORE</div>
  </div>
  <div class="card" style="left:452px;top:417px">
    <svg width="54" height="54" viewBox="0 0 54 54" fill="none" stroke="var(--orange)" stroke-width="2.2"><circle cx="27" cy="10" r="6"/><ellipse cx="27" cy="32" rx="18" ry="13"/><path d="M16 42 v6 M36 42 v6 M45 30 h5"/><circle cx="20" cy="29" r="1" fill="var(--orange)"/></svg>
    <h4>Financial Accountability</h4>
    <p>Lorem ipsum, or lipsum as it is sometimes known, is dummy text used in laying out print, graphic or web designs.</p>
    <div class="btn">READ MORE</div>
  </div>
  <div class="card" style="left:777px;top:417px">
    <svg width="54" height="54" viewBox="0 0 54 54" fill="none" stroke="var(--orange)" stroke-width="2.2"><rect x="6" y="6" width="42" height="32"/><path d="M27 2 v4 M16 50 l6-12 M38 50 l-6-12"/><path d="M16 20 a6 6 0 1 0 6-6 v6z"/><path d="M28 14 h14 M28 20 h14 M12 30 h30"/></svg>
    <h4>Reporting and Monitoring</h4>
    <p>Lorem ipsum, or lipsum as it is sometimes known, is dummy text used in laying out print, graphic or web designs.</p>
    <div class="btn">READ MORE</div>
  </div>
</section>

<p class="abs blog-lead">Visit our blog for the latest in senior care news.</p>
<div class="abs btn-outline blog-btn">VISIT OUR BLOG</div>

<article class="abs post" style="left:125px">
  <div class="abs" role="img" aria-label="Children playing with puzzle pieces at a table, green tint" style="left:0;top:0;width:456px;height:255px;background:linear-gradient(135deg,#7fbd52,#5ea63a 55%,#86b65a)"></div>
  <div class="date"><b>15</b><span>Jan</span></div>
  <h5>Lorem ipsum, or lipsum as it is sometimes known</h5>
  <p>Lorem ipsum, or lipsum as it is sometimes known ...</p>
  <div class="more">READ MORE <span>›</span></div>
</article>
<article class="abs post" style="left:617px">
  <div class="abs" role="img" aria-label="Smiling woman at a playground, green tint" style="left:0;top:0;width:456px;height:255px;background:linear-gradient(135deg,#4f9a36,#6aab45 50%,#3f8a2e)"></div>
  <div class="date"><b>20</b><span>Jan</span></div>
  <h5>Lorem ipsum, or lipsum as it is sometimes known</h5>
  <p>Lorem ipsum, or lipsum as it is sometimes known ...</p>
  <div class="more">READ MORE <span>›</span></div>
</article>

<div class="abs quote-mark">“</div>
<div class="abs t-name">Daniel Foster</div>
<div class="abs t-role">Professor, Denmark</div>
<svg class="abs" style="left:107px;top:2535px" width="22" height="40" viewBox="0 0 22 40"><path d="M20 2 L3 20 L20 38" fill="none" stroke="#f5a764" stroke-width="3.5"/></svg>
<svg class="abs" style="left:1072px;top:2535px" width="22" height="40" viewBox="0 0 22 40"><path d="M2 2 L19 20 L2 38" fill="none" stroke="#f5a764" stroke-width="3.5"/></svg>
<p class="abs t-text">Lorem ipsum, or lipsum as it is sometimes known, is dummy text used in laying out print, graphic or web designs. The passage is attributed to an unknown typesetter in the 15th century who is thought to have scrambled parts of Cicero's De Finibus Bonorum et Malorum for use in a type specimen book.</p>
<div class="abs dots"><i></i><i class="on"></i><i></i><i></i></div>
<div class="abs btn-solid">VIEW FEEDBACK</div>
<div class="abs btn-outline btn-testi">VIEW TESTIMONIALS</div>

<footer class="abs site-footer">
  <div class="co">Bright Meadow Care Partners LLC</div>
  <div class="addr">Adress: Your company address goes here | Phone: 000 555 0142 | Fax: 000 555 0199</div>
  <div class="copy">© bright meadow care partners llc privacy policy</div>
</footer>

</body>
</html>
```